Tau Omicron civil engineering orgnization activities flyer

we need flyer design for Tau Omicron civil engineering honor society in Halverton College for mining and industry. the flyer contain the schedule of the expected activity. the design should have a purple color and Tau Omicron Key and logo (you will find them in the attached file) and the design should have something referring to civil engineering

Industry/Entity Type

Education

Colors
6b449b

Requirements
Must have
• Tau Omicron logo, key, motto
Nice to have
• civil engineering samples, purple color

```html
<!DOCTYPE html>
<html lang="en">
<head>
<meta charset="utf-8">
<title>Tau Omicron Activities Flyer</title>
<link href="https://fonts.googleapis.com/css2?family=Cinzel:wght@400;700&family=Lato:wght@400;700;900&display=swap" rel="stylesheet">
<style>
:root{
  --purple:#6b449b;
  --purple-deep:#4d2a86;
  --purple-bright:#7a3fc0;
  --black:#17161a;
  --white:#ffffff;
  --grey:#e9e9ec;
  --ink:#222;
}
*{margin:0;padding:0;box-sizing:border-box}
html,body{width:907px;height:1200px;overflow:hidden;background:#f2f2f2}
.flyer{position:relative;width:907px;height:1200px;overflow:hidden;background:var(--white);font-family:'Lato',sans-serif}
.shapes{position:absolute;inset:0}
.brand{position:absolute;left:0;top:58px;width:555px;text-align:center;color:var(--white)}
.brand-name{font-family:'Cinzel',serif;font-weight:400;font-size:44px;letter-spacing:1px;display:inline-flex;align-items:center;gap:14px}
.brand-name::before{content:"";width:22px;height:22px;background:var(--white);display:inline-block}
.brand-tag{font-size:12px;margin-top:2px;padding-left:90px}
.photo{position:absolute;left:0;top:138px;width:515px;height:340px;
  clip-path:polygon(0 0,100% 0,88% 100%,0 100%);
  background:linear-gradient(135deg,#6d5440 0%,#a98a66 35%,#3c4f86 60%,#c9d35a 82%,#5a4a3a 100%)}
.motto-title{position:absolute;left:592px;top:50px;font-family:'Cinzel',serif;font-weight:700;font-size:38px;color:var(--purple-bright);letter-spacing:1px}
.motto-text{position:absolute;left:480px;top:110px;width:410px;height:388px;color:var(--white);font-size:19px;line-height:27px;text-align:justify;text-align-last:right;letter-spacing:.5px;hyphens:auto}
.motto-text .edge{float:left;width:90px;height:388px;shape-outside:polygon(0 0,88px 0,10px 388px,0 388px)}
.meeting-bg{position:absolute;left:0;top:497px;width:907px;height:360px;background:radial-gradient(ellipse at 55% 50%,#ffffff 0%,#e6e6ea 60%,#d6d6dc 100%)}
.meeting-tab{position:absolute;left:0;top:505px;width:245px;height:30px;background:var(--black);clip-path:polygon(0 0,88% 0,100% 100%,0 100%);
  color:var(--white);font-family:'Cinzel',serif;font-weight:700;font-size:19px;letter-spacing:2px;padding:3px 0 0 45px}
.schedule{position:absolute;left:140px;top:545px;width:620px;border:3px solid var(--purple);border-spacing:4px;background:var(--white);
  font-size:11.5px;font-weight:900;color:var(--purple-deep);text-align:center;text-transform:uppercase}
.schedule th,.schedule td{border:3px solid var(--purple);height:31px;padding:0 3px;line-height:1.1}
.schedule td{color:var(--ink);font-size:12.5px}
.schedule td.small{font-size:11px}
.service{position:absolute;left:35px;top:888px;width:420px;color:var(--white)}
.service h2{font-family:'Cinzel',serif;font-weight:400;font-size:22px;letter-spacing:1.5px;margin-bottom:6px}
.service ul{list-style:none;font-size:12.5px;line-height:16px}
.service li{position:relative;padding-left:16px;margin-bottom:5px}
.service li::before{content:"";position:absolute;left:0;top:5px;width:7px;height:7px;background:var(--white)}
.service h2.social{margin-top:8px}
.initiation{position:absolute;left:530px;top:870px;width:360px;text-align:center;font-size:13.5px;line-height:17px;color:var(--ink)}
.initiation .hl{color:var(--purple-bright);font-weight:900}
.initiation .bold{font-weight:900;font-size:14.5px}
.contact{position:absolute;left:500px;top:1012px;width:407px;height:150px;background:var(--black);padding:22px 0 0 40px;color:var(--white)}
.contact dt{font-family:'Cinzel',serif;font-weight:700;font-size:14px;color:var(--purple-bright);letter-spacing:1px}
.contact dd{font-weight:700;font-size:16px;margin-bottom:10px;letter-spacing:.3px}
</style>
</head>
<body>
<main class="flyer">
  <svg class="shapes" width="907" height="1200" viewBox="0 0 907 1200" aria-hidden="true">
    <rect x="0" y="0" width="907" height="497" fill="var(--purple-deep)"/>
    <polygon points="560,0 907,0 907,497 462,497" fill="var(--white)"/>
    <polygon points="572,0 907,0 907,497 474,497" fill="var(--black)"/>
    <polygon points="0,855 432,855 505,1200 0,1200" fill="var(--purple-deep)"/>
    <polygon points="0,855 432,855 438,880 0,880" fill="var(--purple)" opacity=".7"/>
    <rect x="505" y="1165" width="402" height="35" fill="var(--white)"/>
  </svg>

  <header class="brand">
    <div class="brand-name">Tau Omicron</div>
    <div class="brand-tag">The Civil Engineering Honor Society</div>
  </header>

  <div class="photo" role="img" aria-label="Students in hard hats building a timber frame on a service project"></div>

  <h1 class="motto-title">OUR MOTTO</h1>
  <p class="motto-text"><span class="edge"></span>Dedicated to the purpose of maintaining and promoting the status of civil engineering as an ideal profession, Tau Omicron was organized to recognize the characteristics of the individual civil engineer deemed to be fundamental to the successful pursuit of an engineering career, and to aid in the development of those characteristics in the civil engineering student</p>

  <div class="meeting-bg" role="img" aria-label="Soft grey engineering backdrop"></div>
  <div class="meeting-tab">MEETING</div>

  <table class="schedule">
    <thead>
      <tr><th>Meeting No.</th><th>Date</th><th>Time</th><th>Location</th><th>Name</th><th>Company</th></tr>
    </thead>
    <tbody>
      <tr><td>1</td><td>9/8/2015</td><td>7 PM</td><td>BCH 124</td><td class="small">Dr. Ferrant</td><td>-</td></tr>
      <tr><td>2</td><td>9/22/2015</td><td>7 PM</td><td>BCH 124</td><td class="small">Dale Pruett</td><td class="small">Metro Waterworks</td></tr>
      <tr><td>3</td><td>10/6/2015</td><td>7 PM</td><td>BCH 124</td><td class="small">Owen Hartley</td><td class="small">Camp Ridgeford</td></tr>
      <tr><td>4</td><td>10/20/2015</td><td>7 PM</td><td>BCH 124</td><td class="small">Casey Brennan</td><td class="small">Norvale Inc.</td></tr>
      <tr><td>5</td><td>11/3/2015</td><td>7 PM</td><td>BCH 124</td><td class="small">Scavenger Hunt</td><td class="small">Social</td></tr>
      <tr><td>6</td><td>11/17/2015</td><td>7 PM</td><td>BCH 124</td><td class="small">Nomination/ Gil Marsden</td><td class="small">Ashby Partners</td></tr>
      <tr><td>7</td><td>12/1/2015</td><td>7 PM</td><td>BCH 124</td><td class="small">Elections</td><td>-</td></tr>
    </tbody>
  </table>

  <section class="service">
    <h2>SERVICE</h2>
    <ul>
      <li><b>Kestrel Nature Reserve Service Day</b> / Saturday, Oct 24, 11 am / Kestrel Nature Reserve, Ashford, MO 65000, United States</li>
      <li><b>Community Partnership Service Day</b> / Saturday, Nov 7, 11 am / The Neighbors Thrift Shop, 310 N Quarry Ave, Ashford, MO 65000, United States</li>
      <li><b>Tri Valley Animal Shelter Volunteer Day</b> / Thursday, Nov 12, 12 pm / Tri Valley Animal Shelter, 58 E Millbrook St, Ashford, MO 65000, United States</li>
    </ul>
    <h2 class="social">SOCIAL</h2>
    <ul>
      <li><b>Tau Omicron Smoker</b><br><b>Bowling</b> / Starline Lanes (212 Elm Road)/ Wednesday, October 28th /9:00 PM</li>
      <li><b>Plaque Signing</b>/ When: December 8th / the Zone</li>
    </ul>
  </section>

  <div class="initiation">
    <div class="hl">12/12/2015 5PM-6PM BCH314</div>
    <div class="hl">Initiation diner 6:30PM</div>
    <div class="hl">Marlowe's 420 West Cedar Lane Ashford</div>
    <div class="bold">Tuesday, September 29th</div>
    <div class="bold">at Noon in BCH 120</div>
    <div>Initiation diner / Marlowe's</div>
    <div>420 West Cedar Lane</div>
    <div>Ashford</div>
  </div>

  <dl class="contact">
    <dt>Campus Hub:</dt>
    <dd>https://campushub.example/chapter</dd>
    <dt>Social Page:</dt>
    <dd>https://social.example/tau.hcmi</dd>
  </dl>
</main>
</body>
</html>
```